I need a great design for my Ebook because that will help spread the message

Hey there,

I wrote an eBook (THE MORNING LANTERN METHOD) about how confidence impacts one's life, why it’s important and how to get more of it and I need someone to design it nicely.

My target audience is made up of more women than men.

I have pictures for each one of the 7 steps in the book, but I am open to your suggestions.

I really like Optima as a font. I have a bit of gold in the text. I would be happy if you could keep it. You can format the text as you think best.

I'd love a modern design.

I added an old design of the ebook for you to see the way the pictures are used for each step because I want to keep that blend between the picture and the title of the step.
I like the idea of each step starting on a new page and the block footer - just not black.

I want the subtitle of each step to be a different font to the title.

Please ask any questions you have.

Thank you!

Target Market(s)

Men and women aged 25-45.

Industry/Entity Type

Life Coaching

Font styles to use
Sans Serif

Colors
ffffff

Requirements
Must have
• My brand colours only:
• navy #233264
• white
• light pink #fff3f1
• mustard yellow #ffc800.
Nice to have
• The pictures I uploaded for each step.
Should not have
• Should not have much black.

```html
<!DOCTYPE html>
<html lang="en">
<head>
<meta charset="utf-8">
<title>The Morning Lantern Method</title>
<link rel="stylesheet" href="https://fonts.googleapis.com/css2?family=Marcellus&family=Josefin+Sans:wght@300;600&display=swap">
<style>
  :root {
    --navy: #233264;
    --gold: #ffc800;
    --frame-gold: #f2b705;
    --white: #ffffff;
    --pink: #fff3f1;
    --sky: #cfe3ef;
    --stone: #b9bcc0;
  }
  html, body {
    margin: 0;
    padding: 0;
    width: 800px;
    height: 1200px;
    overflow: hidden;
    background: var(--white);
  }
  .cover {
    position: relative;
    width: 800px;
    height: 1200px;
    overflow: hidden;
  }
  .cover__backdrop {
    position: absolute;
    inset: 0;
    background: linear-gradient(180deg,
      #e9c9a2 0%, #d9b48f 8%,
      #c7cacd 14%, var(--stone) 30%,
      #d6d8db 45%, #c9c2bd 55%,
      #e7ddd2 62%, #e3a36a 70%,
      #eef1f3 78%, var(--sky) 88%,
      #b8d4e8 100%);
  }
  .cover__veil {
    position: absolute;
    left: 36px;
    top: 56px;
    width: 728px;
    height: 1088px;
    background: linear-gradient(180deg,
      rgba(255,255,255,0.55) 0%,
      rgba(255,255,255,0.72) 40%,
      rgba(255,255,255,0.78) 70%,
      rgba(255,255,255,0.62) 100%);
  }
  .cover__frame {
    position: absolute;
    left: 36px;
    top: 56px;
    width: 728px;
    height: 1088px;
    box-sizing: border-box;
    border: 3px solid var(--frame-gold);
    box-shadow: 1px 1px 3px rgba(35,50,100,0.35);
  }
  .title {
    position: absolute;
    left: 0;
    width: 800px;
    margin: 0;
    text-align: center;
    font-family: "Marcellus", "Optima", sans-serif;
    font-weight: 400;
    line-height: 1;
  }
  .title__line {
    position: absolute;
    left: 0;
    width: 800px;
    display: block;
  }
  .title__line--gold {
    color: var(--gold);
    text-shadow: 3px 3px 0 var(--navy);
  }
  .title__line--navy {
    color: var(--navy);
    text-shadow: 3px 3px 0 var(--gold);
  }
  .title__the { top: 128px; font-size: 92px; }
  .title__morning { top: 328px; font-size: 96px; letter-spacing: 1px; }
  .title__lantern { top: 540px; font-size: 90px; }
  .title__method { top: 756px; font-size: 90px; }
  .author {
    position: absolute;
    left: 0;
    top: 1060px;
    width: 800px;
    text-align: center;
    font-family: "Josefin Sans", sans-serif;
    font-size: 46px;
    letter-spacing: 8px;
    color: var(--navy);
    line-height: 1;
  }
  .author__first { font-weight: 300; }
  .author__last { font-weight: 600; }
</style>
</head>
<body>
  <main class="cover">
    <div class="cover__backdrop" role="img" aria-label="Photo collage of the seven steps: stacking toys, workbench tools, the word forgiveness written in sand, a studio microphone, autumn pumpkins spelling thanks, a woman meditating and hot air balloons in a blue sky"></div>
    <div class="cover__veil"></div>
    <div class="cover__frame"></div>

    <h1 class="title">
      <span class="title__line title__line--gold title__the">The</span>
      <span class="title__line title__line--navy title__morning">MORNING</span>
      <span class="title__line title__line--gold title__lantern">LANTERN</span>
      <span class="title__line title__line--gold title__method">METHOD</span>
    </h1>

    <p class="author"><span class="author__first">MARLO</span><span class="author__last">HENSLEY</span></p>
  </main>
</body>
</html>
```